Major Australian Food and Wine Event Web Design Project

The project will consist of 3 designs
The homepage
A city hub page
A general content page

The main audience who will visit the website will be (in Order of importance:

1) Visitors
- Mainly women 24 – 54 years (they are the main ticket buyers)
- In a relationship – so will go to the show with their partner
- In a good paying job or home maker – and who have disposable income to spend $30 a ticker
- Enjoy food, wine and going out
- Looking for a fun day out – although an event that is about food and wine – it is an event that most people will go to and have a fun day out – not too pretentious

A smaller proportion of the audience will be:
2) Exhibitors & sponsors ( both prospective and existing)
3) Media

Objectives:

- Functionality on home page and sub pages needs to be updated, clear, easy to navigate and inject a sense of ‘fun’ – need to make it look more professional
- Need to incorporate the many things that need to be on the home page and sub pages in a visually appealing manner
- Ensure the ‘Cons’ above are considered and reflected in functionality and design
- To not be too focus on the colours (these can be changed) – but focus on the functionality and overall design opportunities.

Approach:

Keywords to describe the Bright Plate & Vine Fair:
Fun day out, discover, learn, indulge, entertaining

Other website examples:

Some great consumers event websites from the UK really make our website look basic and juvenile – and below are some examples of the presentation of how we would like our website to look like:

http://www.morselfairs-example.com/london/ This website is clean, includes good social media integration and exudes a sense of fun. Their content pages, such as the features landing page also presents options in a clear and visually appealing way with a series of boxes including image and text http://www.morselfairs-example.com/london/content/343/Features

http://www.homecraftexpo-example.com/ - this is also a great website – and it incorporates all the elements we would be looking for on our homepage – but the background/skin also includes a sense of fun and cheekiness. Subpages also are consistent.

Features

• Its a fun day that offers great value for money
• Caters to all visitors, regardless of different levels of knowledge or interest in food, wine and cooking.
• Sample great quality food and wine products from hundreds of reputable exhibitors
• Learn more through many of the shows feature activities (Celeb Theatre, Wine Theatre, Cooking & Cheese Classes)

Functionality & Structure:

In a user friendly, easy to view way, we need to incorporate the following functionality elements on home page:
- main header (that will incorporate our current creative) with a ‘fun’ skin
- navigation tabs/references (hone, location, tickets, blog, sign up, exhibitors)
- navigation/content banner (rotating)
- Area for small intro about the show
- News and highlight section
- New exhibitors section
- Obvious Ticket call to action
- Obvious sign up call to action
- Social media buttons or links ( really like the moving gifs on the Homecraftexpo-example.com site
- area for advertising (MREC size) to sell to exhibitors/sponsors
- Show dates for all 5 shows (maybe in main header)

Subpage layout is also important and needs to reflect the homepage – so would also like to see examples of how this would look and tie in with navigation – we generally have a lot of content on these pages, so clear navigation would be useful. – see below for further details of functionality for city Hubs

‘CITY HUB’ BRIEF
When navigating to each location the user will be taken to a ‘CITY HUB’ which should replicate design and content elements of a main HOME page, as well as reflect more specific information for each Show. Elements which must appear on this page are:
• FEATURES – which may be displayed in categories (in boxes, see appendix 1.0) which will link through to relevant content pages. Or in one box which will link through to a features page with all presented in boxes
• CHEFS – may be displayed as a separate icon box which will link to chefs page with bios, Celeb Theatre timetable etc.
• TICKETS – either a button or clear callout to purchase tickets
• PLAN YOUR DAY – may be displayed in a separate content box which will then link through to getting there, sample itineraries and downloadable pocket show guide for visitors to print before coming to the Show.
• WHO’S EXHIBITING – to link back to city specific exhibitor lists

Our current website is out of date and has the following inadequacies (www.brightplatefair-example.com.au) -

The homepage
A city hub page
A general content page

1) Visitors

3) Media

Objectives:

Approach:

To be perceived as a fun, entertaining event with something for everyone - website creative and navigation must reflect this.

Other website examples:

Features

- New exhibitors section

‘CITY HUB’ BRIEF

- Dated design/layout
- Homepage too text heavy
- No content boxes that can be used for different features/areas (eg. News, Exhibitors etc)
- Uninspiring colours and skin(eg. grey background), does not reflect ‘a fun day out’
- Limited presence of social media platforms and lacks ‘community’
- No continuity in sub pages
- main banner too big – takes up too much space on homepage

Requirements
Must have
• As per above brief.

In addition:
Floating social media buttons on side
Wrap around image
Drop down menu (specifically for the location nav item)

```html
<!DOCTYPE html>
<html lang="en">
<head>
<meta charset="utf-8">
<title>Bright Plate &amp; Vine Fair</title>
<link rel="stylesheet" href="https://fonts.googleapis.com/css2?family=Open+Sans:wght@400;600;700&family=Source+Sans+3:wght@400;600;700&family=Kaushan+Script&family=Tinos:ital@1&family=Oswald:wght@500;600&family=Lilita+One&display=swap">
<style>
:root{
  --sky:#4aa3e6;
  --sky-deep:#2d86d2;
  --navy:#0c2d4e;
  --bar:#6fb7ee;
  --panel:#ffffff;
  --grey-band:#e3e7ea;
  --grey-line:#d4d8db;
  --text:#2b2b2b;
  --muted:#8c8c8c;
  --link:#44a4dc;
  --red:#d8171c;
  --cta-top:#8fd0fb;
  --cta-bottom:#3d9ce6;
}
*{box-sizing:border-box;margin:0;padding:0}
html,body{width:914px;height:1200px;overflow:hidden}
body{
  position:relative;
  font-family:"Open Sans",sans-serif;
  color:var(--text);
  background:radial-gradient(ellipse at 50% 10%,#d4ecfc 0%,var(--sky) 45%,var(--sky-deep) 100%);
}
.abs{position:absolute}

/* header */
.hero-food{left:240px;top:70px;width:215px;height:150px;border-radius:40px 60px 0 0;background:linear-gradient(160deg,#7cbf3a,#6b3a1e 55%,#b5803f)}
.hero-dessert{left:600px;top:40px;width:160px;height:175px;border-radius:50%;background:radial-gradient(circle at 45% 55%,#f6e8c6 0%,#d9b77a 45%,#3a1c0d 80%)}
.ticket-cloud{left:400px;top:34px;width:140px;height:86px;border-radius:50%;background:radial-gradient(circle,#fff 55%,#e9f4fc 100%);display:flex;align-items:center;justify-content:center;text-align:center;font-family:"Lilita One",sans-serif;font-size:20px;line-height:25px;color:var(--navy)}
.page{left:114px;top:196px;width:686px;height:800px;background:var(--panel)}
.page-tab{left:96px;top:210px;width:18px;height:60px;background:#8dc63f}
.navbar{left:96px;top:219px;width:722px;height:38px;background:linear-gradient(#9fd1f6,var(--bar));border-bottom:1px solid #4b99d8}
.navbar-fold-l{left:96px;top:257px;width:0;height:0;border-top:14px solid var(--navy);border-left:18px solid transparent}
.navbar-fold-r{left:800px;top:257px;width:0;height:0;border-top:14px solid var(--navy);border-right:18px solid transparent}
.nav{left:384px;top:224px;display:flex;gap:36px;font-family:"Kaushan Script",cursive;font-size:21px;color:var(--navy)}
.search{left:661px;top:228px;width:111px;height:23px;border-radius:12px;background:var(--navy);color:#8ea4b9;font-size:9px;padding:5px 14px;font-style:italic}
.search svg{position:absolute;right:9px;top:5px}
.logo-card{left:134px;top:147px;width:146px;height:131px;border-radius:12px;background:#fff;box-shadow:0 2px 6px rgba(0,0,0,.25);display:flex;align-items:center;justify-content:center;text-align:center;font-weight:700;font-size:17px;line-height:21px;color:var(--navy)}

/* main column */
.slider{left:130px;top:288px;width:446px;height:190px;background:var(--navy)}
.slider-photo{width:446px;height:143px;background:linear-gradient(120deg,#5b4a3a,#c49a7a 40%,#c0303a 75%,#3a2a22)}
.slider-caption{position:absolute;left:10px;top:152px;font-family:"Tinos",serif;font-style:italic;font-size:22px;color:#fff}
.dots{position:absolute;right:14px;top:160px;display:flex;gap:5px}
.dots span{width:7px;height:7px;border-radius:50%;background:#fff}
.dots span:first-child{background:none;border:1.5px solid #fff}
.intro-title{left:130px;top:488px;width:446px;height:26px;background:var(--navy);clip-path:polygon(0 0,100% 0,94% 50%,100% 100%,0 100%);font-family:"Tinos",serif;font-style:italic;font-weight:400;font-size:16px;color:#fff;padding:3px 8px;white-space:nowrap}
.intro{left:133px;top:519px;width:432px;font-size:10.2px;line-height:13px;letter-spacing:-.1px}
.intro p{margin-bottom:13px}
.intro .signup-link{color:var(--red)}

.panel-head{background:linear-gradient(#fff,var(--grey-band));font-family:"Source Sans 3",sans-serif;font-weight:700;font-size:14px;color:var(--navy);border-bottom:1px solid var(--grey-line)}
.updates{left:133px;top:706px;width:432px;height:256px;border:1px solid var(--grey-line)}
.updates .panel-head{height:32px;padding:6px 6px}
.updates-inner{position:absolute;left:7px;top:36px;width:416px;height:210px;border:1px solid var(--grey-line)}
.tabs{position:absolute;left:4px;top:4px;display:flex;gap:2px}
.tabs span{background:var(--sky-deep);color:#fff;font-size:10.5px;padding:2px 12px;border:1px solid var(--navy)}
.tabs span.active{background:var(--navy)}
.tab-rule{position:absolute;left:4px;top:23px;width:403px;height:3px;background:var(--navy)}
.event{position:absolute;display:flex;gap:6px;width:200px;align-items:flex-start}
.event-mark{width:40px;flex:none;font-size:6.5px;line-height:7.5px;font-weight:700;color:var(--navy)}
.event-name,.event-date{font-size:9.8px;line-height:13px;white-space:nowrap}
.event-name{color:var(--link)}
.event-date{color:var(--muted)}
.event-sep{position:absolute;height:1px;background:var(--grey-line);width:195px}
.event-col{position:absolute;left:209px;top:38px;width:1px;height:164px;background:var(--grey-line)}

/* sidebar */
.box{position:absolute;left:588px;width:196px;border:1px solid var(--grey-line);background:#fff}
.box .panel-head{height:32px;padding:5px 6px}
.social{top:288px;height:83px}
.social-icons{display:flex;gap:22px;padding:12px 0 0 17px}
.social-icons span{width:22px;height:26px;border-radius:4px;background:var(--sky-deep)}
.social-icons span:nth-child(3){background:#c4262b}
.social-icons span:nth-child(4){background:#6b3fa0}
.feed{top:380px;height:83px}
.feed .panel-head{padding-left:36px}
.feed .bird{position:absolute;left:6px;top:4px;width:22px;height:22px;border-radius:50%;background:var(--sky-deep)}
.feed-body{display:flex;gap:8px;padding:8px 6px;font-size:7.3px;line-height:9.5px}
.feed-mark{width:44px;flex:none;font-weight:700;font-size:6.5px;line-height:7.5px;color:var(--navy);padding-top:6px}
.book{left:588px;top:486px;width:196px;height:60px;border-radius:4px;background:linear-gradient(var(--cta-top),var(--cta-bottom));border:1px solid #2a7fc4;text-align:center;color:var(--navy);font-family:"Oswald",sans-serif;font-weight:600}
.book .small{font-size:17px;line-height:20px;margin-top:3px}
.book .big{font-size:26px;line-height:30px;display:flex;justify-content:center;align-items:center;gap:5px}
.menu{left:588px;top:553px;width:196px}
.menu li{list-style:none;height:28.6px;line-height:28px;padding-left:26px;font-family:"Source Sans 3",sans-serif;font-weight:600;font-size:12.5px;color:var(--navy);background:linear-gradient(#fff,var(--grey-band));border:1px solid var(--grey-line);border-top:none}
.menu li:first-child{border-top:1px solid var(--grey-line)}
.newsletter{top:707px;height:160px}
.newsletter .panel-head{text-align:center;padding-top:6px}
.newsletter p{font-size:8.2px;line-height:11px;color:var(--muted);padding:11px 8px 0}
.field{margin:9px 0 0 8px;width:176px;height:23px;border:1px solid var(--grey-line);font-size:8.5px;color:var(--muted);padding:5px 10px}
.field + .field{margin-top:4px}
.signup-btn{position:absolute;right:12px;bottom:9px;background:var(--navy);color:#fff;font-size:9.5px;padding:5px 14px}
.gallery{left:588px;top:877px;width:196px;height:84px;background:linear-gradient(150deg,#3f6f2e,#8a6a9a 45%,#c99a5a 80%,#4a3a2e)}
.gallery-text{position:absolute;left:8px;bottom:4px;color:#fff;font-size:8.5px;line-height:11px}
.gallery-text strong{display:block;font-family:"Source Sans 3",sans-serif;font-size:13px;line-height:14px}

/* floating share */
.share{left:868px;top:263px;width:46px;height:190px;background:#fff;border-radius:4px 0 0 4px;box-shadow:0 0 3px rgba(0,0,0,.25);display:flex;flex-direction:column;align-items:center;gap:5px;padding-top:4px;font-size:9px;color:#555}
.share .count{width:38px;border:1px solid #ccc;border-radius:3px;text-align:center;font-weight:700;padding:3px 0}
.share .count.large{font-size:12px}
.share .btn{width:38px;height:14px;border-radius:2px;background:#e4edf6;border:1px solid #b9c9da;font-size:7px;text-align:center;line-height:12px;color:var(--navy)}
.share .round{width:22px;height:22px;border-radius:50%;background:#e8451f}
.share .total{font-size:8px;color:var(--sky-deep);font-weight:700}

/* footer */
.footer{left:96px;top:985px;width:722px;height:170px;background:linear-gradient(#d7ecfc,#6fb5ec);border-bottom:2px solid var(--navy)}
.footer-fold-l{left:96px;top:972px;width:0;height:0;border-bottom:13px solid var(--navy);border-left:18px solid transparent}
.footer-fold-r{left:800px;top:972px;width:0;height:0;border-bottom:13px solid var(--navy);border-right:18px solid transparent}
.footer-photo{left:650px;top:995px;width:160px;height:100px;border-radius:50%;background:radial-gradient(circle,rgba(20,40,70,.35),rgba(20,40,70,0) 70%)}
.f-col{position:absolute;top:1000px;font-size:9.5px;line-height:14.3px;color:#173052}
.f-col h4{font-weight:700;font-size:9.5px;margin-bottom:7px}
.f-col ul{list-style:none}
.f-org{left:598px;top:1054px;font-size:9.5px;line-height:14px;color:#173052}
.f-org strong{display:block;font-size:12px}
</style>
</head>
<body>

<header>
  <div class="abs hero-food" role="img" aria-label="Chocolate cake slice with cinnamon sticks and mint leaves"></div>
  <div class="abs hero-dessert" role="img" aria-label="Chopsticks holding a cheesecake bite with chocolate sauce"></div>
  <div class="abs ticket-cloud">Tickets Now<br>On Sale</div>
</header>

<div class="abs page-tab"></div>
<div class="abs page"></div>
<div class="abs navbar"></div>
<div class="abs navbar-fold-l"></div>
<div class="abs navbar-fold-r"></div>
<nav class="abs nav"><span>Home</span><span>City Hub</span><span>Contact</span></nav>
<div class="abs search">Search..
  <svg width="12" height="12" viewBox="0 0 12 12"><circle cx="5" cy="5" r="3.5" fill="none" stroke="#fff" stroke-width="1.6"/><line x1="7.5" y1="7.5" x2="11" y2="11" stroke="#fff" stroke-width="1.8"/></svg>
</div>
<div class="abs logo-card">Bright Plate<br>&amp; Vine Fair</div>

<main>
  <section class="abs slider">
    <div class="slider-photo" role="img" aria-label="Couple reading a show guide together in a crowd"></div>
    <div class="slider-caption">Succumb to your senses...</div>
    <div class="dots"><span></span><span></span><span></span><span></span><span></span></div>
  </section>

  <h1 class="abs intro-title">The Bright Plate &amp; Vine Fair - all over for another year!</h1>
  <div class="abs intro">
    <p>What a year for good food and wine!</p>
    <p>Melbourne, Sydney, Perth, Adelaide and Brisbane have all had the chance to experience the fun, excitement and joy, that is the Bright Plate &amp; Vine Fair!</p>
    <p>We would like to thank all our amazing visitors for coming along and helping us celebrate another awesome year - A big thank you also to the rest of the crew including exhibitors, sponsors and chefs!</p>
    <p>Make sure you visit the website early next year for all the details of the 2012 Shows - or sign up to our newsletter to be the first to find out when we are on sale and to receive special discounts and offers!</p>
    <p class="signup-link">Sign up to the Bright Plate &amp; Vine Fair e-newsletter</p>
  </div>

  <section class="abs updates">
    <h2 class="panel-head">LATEST UPDATE</h2>
    <div class="updates-inner">
      <div class="tabs"><span class="active">Events</span><span>News</span><span>Blogs</span></div>
      <div class="tab-rule"></div>
      <div class="event-col"></div>
      <div class="event" style="left:4px;top:42px"><div class="event-mark">Bright Plate &amp; Vine Fair</div><div><div class="event-name">Bright Plate of Amsterdam</div><div class="event-date">31 May 2012 to 03 June 2012</div></div></div>
      <div class="event" style="left:214px;top:42px"><div class="event-mark">Bright Plate &amp; Vine Fair</div><div><div class="event-name">Bright Plate of Amsterdam</div><div class="event-date">31 May 2012 to 03 June 2012</div></div></div>
      <div class="event-sep" style="left:4px;top:90px"></div>
      <div class="event-sep" style="left:214px;top:90px"></div>
      <div class="event" style="left:4px;top:105px"><div class="event-mark">Bright Plate &amp; Vine Fair</div><div><div class="event-name">Bright Plate of Amsterdam</div><div class="event-date">31 May 2012 to 03 June 2012</div></div></div>
      <div class="event" style="left:214px;top:105px"><div class="event-mark">Bright Plate &amp; Vine Fair</div><div><div class="event-name">Bright Plate of Amsterdam</div><div class="event-date">31 May 2012 to 03 June 2012</div></div></div>
      <div class="event-sep" style="left:4px;top:152px"></div>
      <div class="event-sep" style="left:214px;top:152px"></div>
      <div class="event" style="left:4px;top:167px"><div class="event-mark">Bright Plate &amp; Vine Fair</div><div><div class="event-name">Bright Plate of Amsterdam</div><div class="event-date">31 May 2012 to 03 June 2012</div></div></div>
      <div class="event" style="left:214px;top:167px"><div class="event-mark">Bright Plate &amp; Vine Fair</div><div><div class="event-name">Bright Plate of Amsterdam</div><div class="event-date">31 May 2012 to 03 June 2012</div></div></div>
    </div>
  </section>
</main>

<aside>
  <section class="box social">
    <h2 class="panel-head">SOCIALISE WITH US</h2>
    <div class="social-icons"><span></span><span></span><span></span><span></span></div>
  </section>
  <section class="box feed">
    <div class="bird"></div>
    <h2 class="panel-head">CHIRPER FEED</h2>
    <div class="feed-body">
      <div class="feed-mark">Bright Plate &amp; Vine Fair</div>
      <p>Its February, so treat yourself! Buy 2 Homecraft Live Expo tickets for just £20. visit http://www.brightplatefair-example.com.au/</p>
    </div>
  </section>
  <div class="abs book">
    <div class="small">BOOK NOW &amp; SAVE £££S</div>
    <div class="big">CLICK HERE
      <svg width="30" height="20" viewBox="0 0 30 20"><path d="M0 6h17V0l13 10-13 10v-6H0z" fill="#0c2d4e"/></svg>
    </div>
  </div>
  <ul class="abs menu">
    <li>GET TICKETS</li>
    <li>WANT TO EXHIBIT?</li>
    <li>LIKE US ON FRIENDSPACE</li>
    <li>VOLUNTEER FOR THE SHOW</li>
    <li>KEEP UP TO DATE</li>
  </ul>
  <section class="box newsletter">
    <h2 class="panel-head">NEWS LETTER SIGNUP</h2>
    <p>Register to receive our newsletter, bringing you exclusive offers and the latest news.</p>
    <div class="field">Your Name</div>
    <div class="field">Email ID</div>
    <span class="signup-btn">Sign Up!</span>
  </section>
  <div class="abs gallery" role="img" aria-label="Visitors at an outdoor food festival">
    <div class="gallery-text"><strong>Taste 2012 in Pictures</strong>Check out the latest photos from<br>Morsel Fair London 2012</div>
  </div>
</aside>

<div class="abs share">
  <div class="count large">6,032</div>
  <div class="btn">Share</div>
  <div class="count">1k</div>
  <div class="btn">Like</div>
  <div class="count">286</div>
  <div class="btn">+1</div>
  <div class="round"></div>
  <div class="total">25K</div>
</div>

<footer>
  <div class="abs footer-fold-l"></div>
  <div class="abs footer-fold-r"></div>
  <div class="abs footer"></div>
  <div class="abs footer-photo" role="img" aria-label="Chocolate dessert with dripping sauce"></div>
  <div class="f-col" style="left:140px"><h4>Bright Plate &amp; Vine Fair</h4><ul><li>Home</li><li>Melbourne</li><li>Sydney</li><li>Perth</li><li>Adelaide</li><li>Brisbane</li><li>Want to Exhibit?</li><li>Recipe Club</li></ul></div>
  <div class="f-col" style="left:306px"><h4>Show Attractions</h4><ul><li>Celebrity Theatre</li><li>Cheese Masterclass</li><li>Cooking School</li><li>Decanter Bar</li><li>Restaurant</li><li>Wine Theatre</li><li>Exhibitor list</li><li>Floor plans</li></ul></div>
  <div class="f-col" style="left:456px"><h4>Chef Bio's</h4><ul><li>Ada Greer</li><li>Gavin Mellors</li><li>Greg Castellan</li><li>Marc Fontaine</li><li>Miles Moreton</li><li>Toby Pendleton</li><li>&nbsp;</li><li>Recipe Club</li><li>Login</li></ul></div>
  <div class="abs f-org"><strong>meridian</strong>Event organised by<br><br>Meridian Events Australia.© 2012.<br><br>Competition Terms &amp; Conditions</div>
</footer>

</body>
</html>
```